Carry The Tide Home

Business Card design

Target Market(s)

People who require support in the commnity

Industry/Entity Type

Mental Health Support

Contact Information for Business Card

Mental Health Support Rosalind Bratten carrythetidehome@mailvane.com.au 0481 637 592 PO Box 629 Wattlebrook QLD 4571

Colors
6B429C
8869AF
B7A5CE
E3DAEB
F3F0F8

Requirements
Must have
• Logo & details listed above
Should not have
• No red or orange

```html
<!DOCTYPE html>
<html lang="en">
<head>
<meta charset="utf-8">
<title>Carry The Tide Home – Business Card</title>
<link rel="stylesheet" href="https://fonts.googleapis.com/css2?family=Montserrat:wght@800&family=Open+Sans:wght@400;600&display=swap">
<style>
  :root {
    --stage: #2a2a2e;
    --card-dark: #1f1e23;
    --purple: #6b429c;
    --purple-mid: #8869af;
    --purple-soft: #b7a5ce;
    --yellow: #f2e62a;
    --white: #ffffff;
  }
  * { box-sizing: border-box; margin: 0; padding: 0; }
  html, body { width: 1200px; height: 780px; overflow: hidden; }
  body {
    background: var(--stage);
    font-family: "Open Sans", sans-serif;
    display: flex;
    align-items: center;
    justify-content: center;
    gap: 40px;
  }
  .card {
    position: relative;
    width: 550px;
    height: 314px;
    border-radius: 22px;
    border: 3px solid var(--yellow);
    overflow: hidden;
  }

  /* Back side */
  .card-back { background: var(--purple); }
  .card-back .pattern-field {
    position: absolute; inset: 0;
    background: linear-gradient(200deg, var(--purple-soft) 0%, var(--purple-mid) 28%, var(--purple) 60%, #5a3788 100%);
  }
  .card-back .brand {
    position: absolute;
    right: 34px; top: 126px;
    display: flex; align-items: center; gap: 8px;
  }
  .brand-dot {
    width: 14px; height: 14px; border-radius: 50%;
    background: var(--yellow);
  }
  .brand-name {
    font-family: "Open Sans", sans-serif;
    font-weight: 600;
    font-size: 13px;
    letter-spacing: 1.5px;
    text-transform: uppercase;
    color: var(--white);
  }

  /* Front side */
  .card-front { background: var(--card-dark); }
  .card-front .shapes { position: absolute; inset: 0; width: 100%; height: 100%; }
  .holder {
    position: absolute;
    right: 42px; top: 22px;
    text-align: right;
  }
  .holder-name {
    font-family: "Montserrat", sans-serif;
    font-weight: 800;
    font-size: 28px;
    line-height: 1.1;
  }
  .holder-name .first { color: var(--yellow); }
  .holder-name .last { color: var(--purple); }
  .holder-role {
    font-size: 14px;
    color: var(--white);
    margin-top: 2px;
  }
  .name-tab {
    position: absolute;
    right: 0; top: 0;
    width: 28px; height: 46px;
    background: var(--purple);
  }
  .card-front .brand {
    position: absolute;
    left: 28px; top: 70px;
    display: flex; align-items: center; gap: 10px;
  }
  .card-front .brand-mark {
    width: 58px; height: 58px; border-radius: 50%;
    background: var(--purple);
  }
  .card-front .brand-name { font-size: 14px; }
  .details {
    position: absolute;
    left: 28px; top: 150px;
    color: var(--white);
    font-size: 13.5px;
    line-height: 20px;
  }
  .contact-line { display: flex; align-items: center; gap: 8px; }
  .contact-line svg { width: 13px; height: 13px; flex: none; }
</style>
</head>
<body>

  <section class="card card-back" aria-label="Business card back">
    <div class="pattern-field" role="img" aria-label="Repeating star pattern fading to light purple at the top corner"></div>
    <div class="brand">
      <span class="brand-dot"></span>
      <span class="brand-name">Carry The Tide Home</span>
    </div>
  </section>

  <section class="card card-front" aria-label="Business card front">
    <svg class="shapes" viewBox="0 0 544 308" preserveAspectRatio="none" aria-hidden="true">
      <path d="M544 92 C470 98 438 140 418 222 C398 286 250 296 0 290 L0 308 L544 308 Z" fill="var(--purple)"/>
      <path d="M80 276 C210 286 330 268 402 228 C345 290 220 300 70 290 Z" fill="var(--card-dark)"/>
      <path d="M90 278 C215 286 330 268 398 228 C338 280 220 292 96 286 Z" fill="var(--yellow)"/>
    </svg>

    <div class="name-tab"></div>
    <div class="holder">
      <p class="holder-name"><span class="first">Marisol</span> <span class="last">Quenby</span></p>
      <p class="holder-role">CEO/Director</p>
    </div>

    <div class="brand">
      <span class="brand-mark"></span>
      <span class="brand-name">Carry The Tide Home</span>
    </div>

    <div class="details">
      <p class="service">Mental Health Support</p>
      <p class="contact-person">Rosalind Bratten</p>
      <p class="contact-line">
        <svg viewBox="0 0 16 16"><path d="M4 1.5 L6.5 4.5 L5 6.5 C6 8.5 7.5 10 9.5 11 L11.5 9.5 L14.5 12 L13 14.5 C7 14 2 9 1.5 3 Z" fill="var(--yellow)"/></svg>
        <span>0481 637 592</span>
      </p>
      <p class="contact-line">
        <svg viewBox="0 0 16 16"><rect x="1.5" y="3.5" width="13" height="9" rx="1" fill="none" stroke="var(--yellow)" stroke-width="1.6"/><path d="M2 4 L8 9 L14 4" fill="none" stroke="var(--yellow)" stroke-width="1.6"/></svg>
        <span>carrythetidehome@mailvane.com.au</span>
      </p>
      <p class="contact-line">
        <svg viewBox="0 0 16 16"><path d="M8 15 C4 10 3 8 3 6 A5 5 0 0 1 13 6 C13 8 12 10 8 15 Z" fill="none" stroke="var(--yellow)" stroke-width="1.6"/><circle cx="8" cy="6" r="1.8" fill="var(--yellow)"/></svg>
        <span>PO Box 629 Wattlebrook QLD 4571</span>
      </p>
    </div>
  </section>

</body>
</html>
```